Elegant invitation for prestigious fund raising event

Background
The Lanterns of Willow is a very prestigious fund raising event. It is a sit down dinner, gala type evening with a presentation and auction.
There are three of these event being held at venues around western North Carolina. The areas where these are being held all have one thing in common, they are in the Appalachian Mountains and the craft of quilt making. As you will see from the Concept Boards attached why a mountain theme and quilt “design feel” is being used. One very important point - we don’t want this design to look like an actual quilt.

See the concept board on page 4, which we can’t use that is from another artist but is one good interpretation of the idea and one way to stylize the picture with a “quilt” interpretation and feel. We do not want a literal quilt representation but are looking for an artistic way on how best to interpret what the quilt represents - the feel of “stitching together” the different things across our region that make us all unique but yet bind us all as one.

The Brief:
We want to develop an elegant invitation for these events.
We have develop as save the date (attached) and all we want to use of this is the wording “Lanterns of Willow” we do not like the icon above it.
Also attached is the wording for the invitation, along with the new picture we want to use (taken from the inspiration boards)

Size, fold, color and paper:

Around 5x7 inches, but open to any dimension if you have an idea that will work in a totally different size. Ideally try and stick to something that will fit a standard envelope so that we don’t need to make a special envelope

Fold – up to you if it has a fold or not and which way it folds. Our thought is that it will need a fold to keep it up market but open to any suggestions.
We are happy to print this on a textured paper if you have suggestions. It will be professionally digital printed so the paper needs to be suitable for digital printing

Color. The inspiration boards show the color palette. We have started out in the save the dates with the navy with reversed out white but again totally up to you to use anything from that color palette.
Updates

Target Market(s)

Up market, around 50 - 65 years old, many are retired, very wealthy

Industry/Entity Type

Event

Requirements
Must have
• See brief attached
Nice to have
• See brief attached
Should not have
• See brief attached

```html
<!DOCTYPE html>
<html lang="en">
<head>
<meta charset="UTF-8">
<title>Lanterns of Willow — Invitation</title>
<link rel="stylesheet" href="https://fonts.googleapis.com/css2?family=Cormorant+Garamond:wght@500&family=Didact+Gothic&display=swap">
<style>
  :root {
    --backdrop: #e4e5e7;
    --paper: #ffffff;
    --ink-grey: #6d6e70;
    --ink-soft: #8a8b8d;
    --reverse-white: #ffffff;
    --sky-orange: #f08a2a;
    --sky-amber: #f6b44a;
    --ridge-blue: #4f78b8;
    --ridge-deep: #2f4f8a;
    --forest-green: #3f7a3a;
    --forest-dark: #1f3d25;
    --fold-shade: rgba(0,0,0,0.06);
  }
  * { margin: 0; padding: 0; box-sizing: border-box; }
  html, body {
    width: 1200px; height: 1200px; overflow: hidden;
    background: var(--backdrop);
  }
  .canvas { position: relative; width: 1200px; height: 1200px; }
  .spread {
    position: absolute; left: 60px; width: 1080px; height: 540px;
    display: flex;
    box-shadow: 0 6px 18px rgba(0,0,0,0.12);
  }
  .spread--outer { top: 40px; }
  .spread--inner { top: 620px; background: var(--paper); }
  .panel { position: relative; width: 540px; height: 540px; }
  .landscape-photo {
    position: absolute; inset: 0;
    background:
      linear-gradient(100deg, rgba(31,61,37,0.85) 0%, rgba(63,122,58,0.55) 35%, rgba(63,122,58,0) 60%),
      linear-gradient(180deg,
        #e7702a 0%, var(--sky-orange) 10%, var(--sky-amber) 22%, #d99a5a 30%,
        #5c6fa6 36%, var(--ridge-blue) 48%, #6a8fc8 58%, var(--ridge-deep) 70%,
        #375c6a 80%, var(--forest-green) 90%, var(--forest-dark) 100%);
  }
  .fold-line {
    position: absolute; top: 0; bottom: 0; left: 539px; width: 2px;
    background: var(--fold-shade);
  }
  .spread--inner .panel--left {
    background: linear-gradient(90deg, #ffffff 0%, #ffffff 70%, #f1f1f2 100%);
  }
  .sponsor-name {
    font-family: "Cormorant Garamond", serif;
    font-weight: 500; font-size: 17px; letter-spacing: 0.5px;
    display: flex; align-items: center; gap: 7px;
    position: absolute; white-space: nowrap;
  }
  .sponsor-name .mark-square { display: inline-block; width: 12px; height: 12px; }
  .sponsor-name--reverse { color: var(--reverse-white); left: 230px; top: 232px; }
  .sponsor-name--reverse .mark-square { background: var(--reverse-white); }
  .sponsor-name--grey {
    color: var(--ink-grey);
    left: 50%; top: 50%; transform: translate(-50%, -50%);
  }
  .sponsor-name--grey .mark-square { background: var(--ink-grey); }

  .event-title {
    font-family: "Cormorant Garamond", serif;
    font-weight: 500; font-size: 34px; line-height: 1.15;
    letter-spacing: 1px; text-align: center;
  }
  .event-title--cover {
    position: absolute; left: 0; right: 0; top: 232px;
    color: var(--reverse-white);
  }
  .event-title--inside { color: var(--ink-grey); margin-top: 78px; }

  .invite-copy {
    display: flex; flex-direction: column; align-items: center; text-align: center;
    height: 100%; color: var(--ink-grey);
    font-family: "Didact Gothic", sans-serif;
  }
  .invite-lead {
    font-size: 11px; line-height: 1.45; width: 330px; margin-top: 40px;
    color: var(--ink-soft);
  }
  .invite-details {
    margin-top: 22px; font-size: 19px; line-height: 1.3;
    text-transform: uppercase; letter-spacing: 0.6px;
  }
  .invite-notes {
    margin-top: 18px; font-size: 11px; line-height: 1.45;
    text-transform: uppercase; letter-spacing: 0.6px;
  }
  .invite-notes p + p { margin-top: 12px; }
</style>
</head>
<body>
<main class="canvas">

  <section class="spread spread--outer" aria-label="Invitation outside">
    <div class="landscape-photo" role="img" aria-label="Photograph of Appalachian mountain ridges at sunset, orange sky over blue layered ridges with green pine forest in the foreground"></div>
    <div class="panel panel--left">
      <p class="sponsor-name sponsor-name--reverse"><span class="mark-square"></span>Ridgecrest Valley Hospital</p>
    </div>
    <div class="panel panel--right">
      <h1 class="event-title event-title--cover">Lanterns of Willow</h1>
    </div>
    <div class="fold-line"></div>
  </section>

  <section class="spread spread--inner" aria-label="Invitation inside">
    <div class="panel panel--left">
      <p class="sponsor-name sponsor-name--grey"><span class="mark-square"></span>Ridgecrest Valley Hospital</p>
    </div>
    <div class="panel panel--right">
      <div class="invite-copy">
        <h2 class="event-title event-title--inside">Lanterns of Willow</h2>
        <p class="invite-lead">You are invited to the Second Annual Lanterns of Willow on the plateau. Please join us for an elegant and entertaining affair benefiting the healthcare in our region.</p>
        <div class="invite-details">
          <p>6th of June, 2016</p>
          <p>The Farm at Laurel Creek Inn</p>
          <p>Beginning at 5:30pm</p>
        </div>
        <div class="invite-notes">
          <p>Cocktail Attire • Valet Parking</p>
          <p>All proceeds from the night will go to<br>benefit Ridgecrest Valley Hospital</p>
        </div>
      </div>
    </div>
    <div class="fold-line"></div>
  </section>

</main>
</body>
</html>
```